Bright Lanterns Business Card

Design of business cards

Target Market(s)

We are aiming as small business owners who need anything from basic business structures, website plans, business processes and quality assurance.

Industry/Entity Type

Business

Colors

Designer to choose colors to be used in the design.

Requirements
Nice to have
• I would prefer one side of the card to use the green from the logo. Prefer to have the same font as the logo.

```html
<!DOCTYPE html>
<html lang="en">
<head>
<meta charset="UTF-8">
<title>Bright Lanterns Consulting – Business Cards</title>
<link href="https://fonts.googleapis.com/css2?family=Cinzel:wght@400;500&family=Open+Sans:wght@400&display=swap" rel="stylesheet">
<style>
  :root {
    --brand-green: #97bd33;
    --ink-grey: #3c3c3c;
    --soft-grey: #5a5a5a;
    --paper: #ffffff;
    --backdrop: #e9e9e9;
  }
  * { box-sizing: border-box; margin: 0; padding: 0; }
  html, body { width: 1200px; height: 795px; overflow: hidden; }
  body {
    background: var(--backdrop);
    display: flex;
    align-items: center;
    justify-content: center;
    gap: 40px;
  }
  .card {
    position: relative;
    width: 520px;
    height: 297px;
    background: var(--paper);
    overflow: hidden;
  }
  .brand-name {
    font-family: "Cinzel", serif;
    font-weight: 500;
    line-height: 1.1;
    letter-spacing: 0.04em;
  }
  .brand-mark {
    display: flex;
    align-items: center;
    gap: 14px;
  }
  .brand-square {
    width: 34px;
    height: 34px;
    flex: none;
  }

  /* front */
  .card-front .top-band {
    position: absolute;
    inset: 0 0 auto 0;
    height: 136px;
    background: var(--brand-green);
    display: flex;
    align-items: center;
    padding-left: 40px;
  }
  .card-front .brand-name { color: var(--paper); font-size: 25px; }
  .card-front .brand-square { background: var(--paper); }
  .person {
    position: absolute;
    left: 40px;
    bottom: 56px;
  }
  .person-name {
    font-family: "Cinzel", serif;
    font-weight: 500;
    font-size: 25px;
    color: var(--brand-green);
    letter-spacing: 0.03em;
  }
  .person-role {
    font-family: "Open Sans", sans-serif;
    font-size: 12px;
    color: var(--soft-grey);
    margin-top: 2px;
    text-align: right;
  }
  .contact-list {
    position: absolute;
    right: 26px;
    top: 150px;
    list-style: none;
    font-family: "Open Sans", sans-serif;
    font-size: 10.5px;
    color: var(--soft-grey);
  }
  .contact-list li {
    display: flex;
    align-items: center;
    gap: 7px;
    height: 18px;
  }
  .contact-icon {
    width: 13px;
    height: 13px;
    flex: none;
  }

  /* back */
  .card-back .bottom-band {
    position: absolute;
    inset: auto 0 0 0;
    height: 160px;
    background: var(--brand-green);
  }
  .card-back .brand-mark {
    position: absolute;
    left: 60px;
    top: 32px;
  }
  .card-back .brand-name { color: var(--ink-grey); font-size: 28px; }
  .card-back .brand-square { background: var(--brand-green); }
</style>
</head>
<body>

  <section class="card card-front" aria-label="Business card front">
    <div class="top-band">
      <div class="brand-mark">
        <span class="brand-square"></span>
        <p class="brand-name">Bright Lanterns<br>Consulting</p>
      </div>
    </div>

    <div class="person">
      <p class="person-name">Daniel Reeve</p>
      <p class="person-role">Managing Director</p>
    </div>

    <ul class="contact-list">
      <li>
        <svg class="contact-icon" viewBox="0 0 13 13" aria-hidden="true"><rect width="13" height="13" rx="2" fill="var(--brand-green)"/><rect x="4" y="2.5" width="5" height="8" rx="1" fill="#fff"/></svg>
        00 004 516 2290
      </li>
      <li>
        <svg class="contact-icon" viewBox="0 0 13 13" aria-hidden="true"><rect width="13" height="13" rx="2" fill="var(--brand-green)"/><path d="M4 3 l2 0 l0.6 2 l-1.1 0.9 a5 5 0 0 0 1.8 1.8 l0.9-1.1 l2 0.6 l0 2 a1 1 0 0 1-1 1 a6 6 0 0 1-6-6 a1 1 0 0 1 0.8-1.2z" fill="#fff"/></svg>
        00 004 516 2290
      </li>
      <li>
        <svg class="contact-icon" viewBox="0 0 13 13" aria-hidden="true"><rect width="13" height="13" rx="2" fill="var(--brand-green)"/><rect x="3" y="5" width="7" height="5" fill="#fff"/><rect x="4.5" y="2.5" width="4" height="2.5" fill="#fff"/></svg>
        00 004 516 2290
      </li>
      <li>
        <svg class="contact-icon" viewBox="0 0 13 13" aria-hidden="true"><rect width="13" height="13" rx="2" fill="var(--brand-green)"/><rect x="2.5" y="4" width="8" height="5.5" fill="#fff"/><path d="M2.5 4 l4 3 l4-3" stroke="var(--brand-green)" stroke-width="0.9" fill="none"/></svg>
        daniel.reeve@mailbox.com.au
      </li>
      <li>
        <svg class="contact-icon" viewBox="0 0 13 13" aria-hidden="true"><rect width="13" height="13" rx="2" fill="var(--brand-green)"/><circle cx="6.5" cy="6.5" r="3.8" fill="none" stroke="#fff" stroke-width="1"/><path d="M2.7 6.5 h7.6 M6.5 2.7 v7.6" stroke="#fff" stroke-width="0.8"/></svg>
        www.sitelink.com.au
      </li>
    </ul>
  </section>

  <section class="card card-back" aria-label="Business card back">
    <div class="brand-mark">
      <span class="brand-square"></span>
      <p class="brand-name">Bright Lanterns<br>Consulting</p>
    </div>
    <div class="bottom-band"></div>
  </section>

</body>
</html>
```